Design a flyer

Hi, I need a flyer designed for an electrical and air conditioning company based in brisbane, Australia.
We service the domestic market.
Flyer is to be double sided
Flyer size DL 210mm X 99mm
Was thinking one side services and discount coupons and the other side possible testimonials.
I have logo uploaded followed with the vehicle advertising, advertising stand alone sign and also business cards.
--------------------------
Coupon Cut out
save $150 OFF switchboard upgrades
save $150 Complimentary Electrical safety inspection
save $50 OFF Air Conditioner install or Service
save $50 next job if you leave feedback for first job
OVER $400 WORTH OF SAVINGS!
Our promise to you
* we will Arrive on time or we will pay you $100
* Before any job begins you will know the exact price
* We will leave your place as clean as we arrived
* if there is a problem and its our fault we will fix it for free
* provide a 12 month warranty on all parts
* we will provide friendly helpful service and advice
Phone number is 0487 625 903
Company Name - Tavolinex
License: 58164
ABN - 61 208 395 172
Also add vornel pay, zund and paklin logo at the bottom
----------------------------
Here is what some of my customers have had to say
Extremely professional...
“Arrived when he said he would, sent through a written quote and was very reasonable. He also checked out our smoke
detectors whist he was here. He installed 2 ceiling fans and an air conditioner. He
cleaned up the mess and was very efficient. I will definitely use him again and recommend
him to family and friends”
R.M – Stretton
“Excellent service provider. He arrived on time with a call before arriving, than carried all jobs quickly and efficiently and left no mess at all. I will definitely recommend his service to others requiring an electrician. Thanks again!”
K.S – Greenslopes
“Over the long weekend, I had problems with my power, not only did you pick up the first phone call but you came out at 5am to fix it. Love the fact you’re a 24hr service!”
T.W – Mount Gravatt
---------------------------
NEW changes
Hi everyone,
Just want to say well done all the designers look great!
I will soon be choosing a winner, but there are a couple of changes i would like to make, if you revise you will be in for a win.
Instead of Save 50 if you leave feedback for the first job quote. I want to change that put $110 cross out and put $71.50 Install & Supply LED Downlights (min 20)
I want this to be the number one followed by switch board upgrade cut out.
Also $50 off air con install - don't put service.
And the third testimonial T.W Make sure it has a full stop
Also keep in mind. It is an electrical & air conditioning company.
Be creative with your design, don't want to see any pictures of people as they are not working for us at this time.
Remember key focus, on coupons, phone numbers, and website. zund and vornelpay can be small and out of the way same with the license numbers.
Thank you
Good Luck!
Target Market(s)
Domestic Market - Home owners
Industry/Entity Type
Air Conditioning

```html
<!DOCTYPE html>
<html lang="en">
<head>
<meta charset="utf-8">
<title>Tavolinex – DL Flyer</title>
<link rel="stylesheet" href="https://fonts.googleapis.com/css2?family=Source+Sans+3:wght@400;600;700&display=swap">
<style>
  :root {
    --orange: #e0692d;
    --blue: #2a6da9;
    --green: #1f8c3b;
    --grey-head: #8e8e8e;
    --grey-dot: #b3b3b3;
    --paper: #f1f1f1;
    --ink: #141414;
    --white: #ffffff;
  }
  * { margin: 0; padding: 0; box-sizing: border-box; }
  html, body { width: 1200px; height: 900px; overflow: hidden; background: var(--white); }
  body { position: relative; font-family: "Source Sans 3", "Myriad Pro", Arial, sans-serif; color: var(--ink); }

  .flyer-side {
    position: absolute; top: 0; width: 422px; height: 895px;
    background: var(--orange); overflow: hidden;
  }
  .flyer-side--front { left: 165px; }
  .flyer-side--back { left: 613px; }
  .side-shapes { position: absolute; inset: 0; }
  .side-content { position: absolute; inset: 0; }

  /* Front: services & coupons */
  .brand-name {
    position: absolute; top: 52px; left: 0; width: 100%;
    text-align: center; font-size: 54px; font-weight: 400;
    color: var(--blue); letter-spacing: 1px;
  }
  .service-title {
    position: absolute; top: 178px; left: 0; width: 100%;
    text-align: center; font-size: 28px; font-weight: 700;
    line-height: 35px; color: var(--grey-head);
  }
  .coupon-title {
    position: absolute; top: 290px; left: 72px;
    font-size: 32px; font-weight: 700; color: var(--green);
  }
  .coupon-list {
    position: absolute; top: 372px; left: 32px; list-style: none;
  }
  .coupon-list li {
    position: relative; padding-left: 17px; height: 25px;
    font-size: 14px; font-weight: 700; color: var(--orange);
  }
  .coupon-list li::before {
    content: ""; position: absolute; left: 0; top: 4px;
    width: 12px; height: 12px; border-radius: 50%; background: var(--grey-dot);
  }
  .savings-total {
    position: absolute; top: 524px; left: 30px;
    font-size: 22px; font-weight: 700; color: var(--blue);
  }
  .promise-title {
    position: absolute; top: 596px; left: 30px;
    font-size: 19px; font-weight: 700; color: var(--ink);
  }
  .promise-list {
    position: absolute; top: 625px; left: 30px; list-style: none;
  }
  .promise-list li {
    height: 24.5px; font-size: 13.4px; font-weight: 700; color: var(--ink);
  }
  .business-ids {
    position: absolute; top: 852px; left: 32px;
    font-size: 12px; font-weight: 700; color: var(--white); line-height: 22px;
  }
  .payment-names {
    position: absolute; top: 858px; left: 206px;
    display: flex; gap: 10px; align-items: center;
  }
  .payment-name {
    display: flex; align-items: center; gap: 4px;
    font-size: 15px; font-weight: 700; color: var(--white);
  }
  .payment-name::before {
    content: ""; width: 10px; height: 10px; background: var(--white);
  }

  /* Back: testimonials */
  .phone-number {
    position: absolute; top: 8px; left: 0; width: 100%;
    text-align: center; font-size: 47px; font-weight: 400;
    color: var(--white); letter-spacing: 1px;
  }
  .testimonial-title {
    position: absolute; top: 142px; left: 24px; width: 390px;
    font-size: 29.5px; font-weight: 700; line-height: 35px; color: var(--blue);
  }
  .testimonial {
    position: absolute; left: 24px; width: 384px;
    font-size: 19.5px; line-height: 22.6px; color: var(--ink);
    hyphens: auto;
  }
  .testimonial--one { top: 219px; }
  .testimonial--two { top: 512px; }
  .testimonial--three { top: 714px; }
  .testimonial-author { display: block; }
</style>
</head>
<body>

<section class="flyer-side flyer-side--front" aria-label="Services and coupons">
  <svg class="side-shapes" width="422" height="895" viewBox="0 0 422 895" aria-hidden="true">
    <rect x="14" y="14" width="393" height="840" fill="var(--paper)"/>
    <path d="M0 895 L0 822 Q 210 845 422 728 L422 895 Z" fill="var(--orange)"/>
    <path d="M14 820 Q 215 842 407 736" fill="none" stroke="var(--blue)" stroke-width="11"/>
  </svg>
  <div class="side-content" lang="en-AU">
    <div class="brand-name">Tavolinex</div>
    <h2 class="service-title">Electrical &amp; Air Conditioning<br>Services</h2>
    <h3 class="coupon-title">Coupon Cut Out</h3>
    <ul class="coupon-list">
      <li>Save $150 OFF switchboard upgrades</li>
      <li>save $150 Complimentary Electrical safety inspection</li>
      <li>save $50 OFF Air Conditioner install or Service</li>
      <li>save $50 next job if you leave feedback for first job</li>
    </ul>
    <p class="savings-total">OVER $400 WORTH OF SAVINGS!</p>
    <h3 class="promise-title">Our promise to you</h3>
    <ul class="promise-list">
      <li>* we will Arrive on time or we will pay you $100</li>
      <li>* Before any job begins you will know the exact price</li>
      <li>* We will leave your place as clean as we arrived</li>
      <li>* if there is a problem and its our fault we will fix it for free</li>
      <li>* provide a 12 month warranty on all parts</li>
      <li>* we will provide friendly helpful service and advice</li>
    </ul>
    <p class="business-ids">License: 58164<br>ABN - 61 208 395 172</p>
    <div class="payment-names">
      <span class="payment-name">vornelpay</span>
      <span class="payment-name">zund</span>
      <span class="payment-name">paklin</span>
    </div>
  </div>
</section>

<section class="flyer-side flyer-side--back" aria-label="Customer testimonials">
  <svg class="side-shapes" width="422" height="895" viewBox="0 0 422 895" aria-hidden="true">
    <rect x="14" y="14" width="394" height="868" fill="var(--paper)"/>
    <path d="M0 0 L422 0 L422 66 Q 230 60 14 136 L0 136 Z" fill="var(--orange)"/>
    <path d="M14 140 Q 230 66 408 78" fill="none" stroke="var(--blue)" stroke-width="8"/>
  </svg>
  <div class="side-content" lang="en-AU">
    <div class="phone-number">0487 625 903</div>
    <h2 class="testimonial-title">Here is what some of my customers have had to say</h2>
    <blockquote class="testimonial testimonial--one">
      Extremely professional...<br>
      “Arrived when he said he would, sent through a written quote and was very reasonable. He also checked out our smoke detectors whist he was here. He installed 2 ceiling fans and an air conditioner. He cleaned up the mess and was very efficient. I will definitely use him again and recommend him to family and friends”
      <span class="testimonial-author">R.M – Stretton</span>
    </blockquote>
    <blockquote class="testimonial testimonial--two">
      “Excellent service provider. He arrived on time with a call before arriving, than carried all jobs quickly and efficiently and left no mess at all. I will definitely recommend his service to others requiring an electrician. Thanks again!”
      <span class="testimonial-author">K.S – Greenslopes</span>
    </blockquote>
    <blockquote class="testimonial testimonial--three">
      “Over the long weekend, I had problems with my power, not only did you pick up the first phone call but you came out at 5am to fix it. Love the fact you’re a 24hr service!”
      <span class="testimonial-author">T.W – Mount Gravatt</span>
    </blockquote>
  </div>
</section>

</body>
</html>
```